Lighting Wholesaler

As our company name is Brenmore Lighting we prefer a Castle as the photo of image, we want a plain glossy plain white back ground, all print to be in black however the company slogan "We Only Wholesale To Projects" to be in blue print, please see attached files to see what we want, This business card is for Darren Hollow and NOT FOR Tom Pardew

Industry/Entity Type

Business

Contact Information for Business Card

Brenmore Lighting Pty Ltd ABN 51 627 913 480
We Only Wholesale To Projects (blue print see attachment)
Darren Hollow
Unit 9, 27 Wattle Rd., Blacktown NSW 2148
Website : www.brenmorelighting-example.com.au
Email : sales@brenmorelighting-example.com.au
Ph : 0491 572 806 Fax : 9812 3059

On Reverse Side as per attachment
Intercoms - Video Audio
Home Security Systems
Commercial Lighting
Domestic Lighting
Fluorescent Lighting
Emergency Lighting
Ventilation Solutions
Exhaust Fan Systems
Xmas Tree Stands (blue print see attachment)

Requirements
Must have
• The business card must be flexible, what I need is a system that will allow me to create using this same template for other people, e.g. this card is for Darren Hollow however we have others in the company and so we will need to change the name, the phone number and the email address of that person. The attached design of my business Card (Tom Pardew) is a layout that I am extremely happy with as it is not congested and it is easy to read but your logo photo may be differrent, if you can find a nicer photo it will be better

```html
<!DOCTYPE html>
<html lang="en">
<head>
<meta charset="utf-8">
<title>Brenmore Lighting – Business Card</title>
<link rel="stylesheet" href="https://fonts.googleapis.com/css2?family=Arimo:wght@400;700&family=Montserrat:wght@600;700&family=Rubik:ital,wght@1,800&family=Tinos&display=swap">
<style>
  :root {
    --page: #e9e7e4;
    --card: #ffffff;
    --ink: #161616;
    --blue: #27239a;
    --mark: #1d1d1d;
    --shadow: rgba(0, 0, 0, 0.18);
  }
  * { box-sizing: border-box; margin: 0; padding: 0; }
  html, body {
    width: 1200px; height: 800px; overflow: hidden;
    background: var(--page);
  }
  .stage { position: relative; width: 1200px; height: 800px; }
  .card {
    position: absolute; top: 241px;
    width: 555px; height: 317px;
    background: var(--card);
    box-shadow: 0 6px 18px var(--shadow);
    color: var(--ink);
  }
  .card--back { left: 30px; }
  .card--front { left: 615px; }

  /* Reverse side */
  .services {
    position: absolute; left: 58px; top: 52px;
    list-style: none;
    font-family: "Arimo", Arial, sans-serif;
    font-weight: 700; font-size: 21px; line-height: 24.5px;
    letter-spacing: 0.3px;
  }
  .services li::before {
    content: "\2022"; display: inline-block; width: 20px;
  }
  .services .services__highlight { color: var(--blue); }

  /* Front side */
  .brand__square {
    position: absolute; left: 24px; top: 46px;
    width: 60px; height: 60px; background: var(--mark);
  }
  .brand__name {
    position: absolute; left: 98px; top: 30px;
    font-family: "Arimo", Arial, sans-serif;
    font-weight: 700; font-size: 43px; line-height: 1;
    color: var(--ink); white-space: nowrap;
  }
  .brand__suffix {
    position: absolute; right: 34px; top: 78px;
    font-family: "Arimo", Arial, sans-serif; font-size: 10px; letter-spacing: 1px;
  }
  .brand__abn {
    position: absolute; left: 170px; top: 92px;
    font-family: "Arimo", Arial, sans-serif; font-size: 10px;
  }
  .slogan {
    position: absolute; left: 30px; top: 112px;
    font-family: "Rubik", Arial, sans-serif;
    font-style: italic; font-weight: 800; font-size: 28px;
    color: var(--blue); white-space: nowrap;
  }
  .person {
    position: absolute; left: 0; right: 0; top: 160px; text-align: center;
    font-family: "Tinos", "Times New Roman", serif;
    font-size: 25px; text-transform: uppercase; letter-spacing: 0.5px;
  }
  .address {
    position: absolute; left: 30px; right: 20px; top: 199px; text-align: center;
    font-family: "Montserrat", Arial, sans-serif; font-weight: 700;
    font-size: 15px; font-variant: small-caps; white-space: nowrap;
  }
  .contact {
    position: absolute; display: flex; align-items: center; gap: 6px;
    font-family: "Montserrat", Arial, sans-serif; font-weight: 600;
    font-size: 13.5px; white-space: nowrap;
  }
  .contact svg { width: 15px; height: 15px; flex: none; }
  .contact--web { left: 110px; top: 226px; }
  .contact--email { left: 110px; top: 248px; }
  .contact--mobile { left: 22px; top: 280px; font-size: 19px; font-weight: 700; }
  .contact--mobile svg { width: 14px; height: 20px; }
  .contact--office { right: 22px; top: 283px; font-size: 15px; }
</style>
</head>
<body>
<main class="stage">

  <section class="card card--back" aria-label="Business card, reverse side">
    <ul class="services">
      <li>Intercoms - Video Audio</li>
      <li>Home Security Systems</li>
      <li>Commercial Lighting</li>
      <li>Domestic Lighting</li>
      <li>Fluorescent Lighting</li>
      <li>Emergency Lighting</li>
      <li>Ventilation Solutions</li>
      <li>Exhaust Fan Systems</li>
      <li class="services__highlight">Christmas Tree Stands</li>
    </ul>
  </section>

  <section class="card card--front" aria-label="Business card, front side">
    <div class="brand__square" aria-hidden="true"></div>
    <div class="brand__name">Brenmore Lighting</div>
    <div class="brand__suffix">PTY. LTD</div>
    <div class="brand__abn">ABN 51 627 913 480</div>

    <p class="slogan">“We Only Wholesale To Projects”</p>
    <p class="person">Darren Hollow</p>
    <p class="address">Unit 9, 27 Wattle Rd., Blacktown NSW 2148</p>

    <p class="contact contact--web">
      <svg viewBox="0 0 16 16" fill="none" stroke="currentColor" stroke-width="1.3" aria-hidden="true">
        <circle cx="8" cy="8" r="6.5"/><ellipse cx="8" cy="8" rx="3" ry="6.5"/><path d="M1.5 8h13M2.5 4.8h11M2.5 11.2h11"/>
      </svg>
      <span>: www.brenmorelighting-example.com.au</span>
    </p>
    <p class="contact contact--email">
      <svg viewBox="0 0 16 16" fill="none" stroke="currentColor" stroke-width="1.3" aria-hidden="true">
        <rect x="1" y="3.5" width="14" height="9.5"/><path d="M1 3.5l7 6 7-6"/>
      </svg>
      <span>: sales@brenmorelighting-example.com.au</span>
    </p>
    <p class="contact contact--mobile">
      <svg viewBox="0 0 14 20" fill="none" stroke="currentColor" stroke-width="1.6" aria-hidden="true">
        <rect x="1.5" y="1" width="11" height="18" rx="1.5"/><path d="M1.5 15h11"/>
      </svg>
      <span>: 0491 572 806</span>
    </p>
    <p class="contact contact--office">
      <svg viewBox="0 0 16 16" fill="none" stroke="currentColor" stroke-width="1.3" aria-hidden="true">
        <circle cx="8" cy="8" r="7"/><path d="M6 4.2c-1.5 1-1.6 3.4 0 5.6s3.5 3 4.8 2.2l-1.2-1.8-1.3.6C7.6 10.2 6.9 9 6.8 8l1.2-.8z" fill="currentColor"/>
      </svg>
      <span>: (612) 9812 3074</span>
    </p>
  </section>

</main>
</body>
</html>
```